Hip-Hop Artist TM Blaze Needs a Album Cover Design

I need an album cover design for my upcoming album. I am a hip-hop artist from Seattle, WA. I have been writing/producing/releases music for the past 15 years. This will be my 4th full length album. For examples of my previous album cover designs and single designs go here --> www.tmblaze-music.net. The title of the album is called "Quiet Harbors". It is an emotional, inspirational album with 18 songs that I wrote and produced over the past 3 years. Some track titles include - "Hold Fast", "Golden Dust". "Kings of Tomorrow", "Burn The Ledger", & "Edge of Winter". I would like the cover to contain something design pattern based, 1 idea would be the blueprint design of a mind processing thoughts - abstract I know. But, feel free to think creatively or out of the box on this as I don't want to give too much direction - you are the graphic artist, not me. I have typically had blues, grays, and blacks in my album covers, but I don't want to put limits on the approach an artist wants to take. Feel free to take this in a direction you think would be interesting.

Reason: I would like to extend the deadline for design submissions in order to have time to provide appropriate feedback to the designers.

Reason: Thank you to everyone that has submitted designs thus far. I truly appreciate you taking the time and sharing your creativity. With the recent design submissions that came in today + the revisions sent yesterday/today, I would like to extend this contest by 5 days - as this album + design means the world to me. I will be providing feedback to the top designers tomorrow. Thank you all again!

```html
<!DOCTYPE html>
<html lang="en">
<head>
<meta charset="utf-8">
<title>TM Blaze – Quiet Harbors</title>
<link rel="stylesheet" href="https://fonts.googleapis.com/css2?family=Orbitron:wght@700;900&display=swap">
<style>
  :root {
    --bg: #000000;
    --ink: #ffffff;
    --glitch-red: #d8303a;
    --glitch-blue: #3a6cff;
    --art-violet: #5a18d8;
    --art-blue: #2a4cf0;
    --art-green: #48e08e;
    --art-orange: #ff7a3c;
  }
  html, body {
    margin: 0;
    padding: 0;
    width: 1200px;
    height: 1200px;
    overflow: hidden;
    background: var(--bg);
  }
  .cover {
    position: relative;
    width: 1200px;
    height: 1200px;
    background: var(--bg);
    overflow: hidden;
    font-family: "Orbitron", sans-serif;
  }
  .cover-art {
    position: absolute;
    inset: 0;
  }
  .artist-name text {
    font-family: "Orbitron", sans-serif;
    font-weight: 900;
    fill: var(--ink);
  }
  .album-title text {
    font-family: "Orbitron", sans-serif;
    font-weight: 700;
    fill: var(--ink);
  }
  .label-mark {
    position: absolute;
    left: 30px;
    top: 1056px;
    width: 124px;
    display: flex;
    flex-direction: column;
    align-items: center;
    gap: 6px;
    color: var(--ink);
    font-family: "Orbitron", sans-serif;
    font-weight: 700;
    text-align: center;
    line-height: 1;
  }
  .label-name { font-size: 16px; letter-spacing: 0.4px; }
  .label-sub { font-size: 12px; letter-spacing: 0.2px; }
  .label-dot {
    width: 76px;
    height: 76px;
    border: 3px solid var(--ink);
    border-radius: 50%;
    box-sizing: border-box;
  }
</style>
</head>
<body>
<main class="cover">
  <svg class="cover-art" width="1200" height="1200" viewBox="0 0 1200 1200" xmlns="http://www.w3.org/2000/svg">
    <defs>
      <radialGradient id="cerebrumGlow" cx="0.5" cy="0.5" r="0.5">
        <stop offset="0" stop-color="var(--art-violet)"/>
        <stop offset="0.35" stop-color="var(--art-blue)"/>
        <stop offset="0.65" stop-color="var(--art-green)" stop-opacity="0.75"/>
        <stop offset="0.85" stop-color="var(--art-orange)" stop-opacity="0.45"/>
        <stop offset="1" stop-color="var(--bg)" stop-opacity="0"/>
      </radialGradient>
      <radialGradient id="hindGlow" cx="0.5" cy="0.5" r="0.5">
        <stop offset="0" stop-color="var(--art-violet)"/>
        <stop offset="0.45" stop-color="var(--art-blue)" stop-opacity="0.85"/>
        <stop offset="0.75" stop-color="var(--art-green)" stop-opacity="0.5"/>
        <stop offset="1" stop-color="var(--bg)" stop-opacity="0"/>
      </radialGradient>
    </defs>

    <g class="mind-illustration" role="img" aria-label="Side view of a human brain whose folds glow in a dense neon pattern of violet, blue, green and orange">
      <ellipse cx="612" cy="560" rx="540" ry="360" fill="url(#cerebrumGlow)"/>
      <ellipse cx="380" cy="960" rx="250" ry="170" fill="url(#hindGlow)"/>
      <ellipse cx="430" cy="1110" rx="110" ry="90" fill="url(#hindGlow)"/>
    </g>

    <g class="artist-name">
      <text x="594" y="186" text-anchor="middle" font-size="168" textLength="1056" lengthAdjust="spacingAndGlyphs" fill="var(--glitch-red)" opacity="0.8" transform="translate(-4 3)">TM BLAZE</text>
      <text x="594" y="186" text-anchor="middle" font-size="168" textLength="1056" lengthAdjust="spacingAndGlyphs" fill="var(--glitch-blue)" opacity="0.8" transform="translate(4 -3)">TM BLAZE</text>
      <text x="594" y="186" text-anchor="middle" font-size="168" textLength="1056" lengthAdjust="spacingAndGlyphs">TM BLAZE</text>
    </g>

    <g class="album-title">
      <text x="596" y="1002" font-size="56" textLength="574" lengthAdjust="spacingAndGlyphs" opacity="0.22" transform="translate(-6 -4)">QUIET HARBORS</text>
      <text x="596" y="1002" font-size="56" textLength="574" lengthAdjust="spacingAndGlyphs">QUIET HARBORS</text>
    </g>
  </svg>

  <div class="label-mark">
    <span class="label-name">TIDEWELL</span>
    <span class="label-dot"></span>
    <span class="label-sub">MUSIC GROUP</span>
  </div>
</main>
</body>
</html>
```